Its just a copy of my concept with little changes.
Be careful you have to come with your unique concept.
All - I'm not sure how some of you are using a prior generation of my logo design, but in the final design (which I did upload for this project), the words in the tagline are flipped so Insight appears first. Please be sure you are using proper version. Thanks! Dot
All - I think the fax number should immediately follow the phone as the numbers are consecutive. Please do not include the cell phone on the letterhead, just on the business card. Appeals, Commercial Litigation (my practice areas) needs to be specified on both. Thanks!
Please note this is a combined project with Hallbrook Law Branding. I'm working with tech support to change the project names so it's clear this is a package. Thanks!
Thanks for all your great work and creativity! This is going to be a hard decison.
Dot

```html
<!DOCTYPE html>
<html lang="en">
<head>
<meta charset="utf-8">
<title>Hallbrook Law – Stationery Set</title>
<link rel="stylesheet" href="https://fonts.googleapis.com/css2?family=Cormorant+Garamond:wght@500&family=Lato:wght@400;700&display=swap">
<style>
  :root{
    --backdrop:#8e8f91;
    --paper:#ffffff;
    --gold:#b48a3c;
    --gold-light:#e6cf97;
    --gold-dark:#8a6424;
    --ink:#5a5a5a;
    --ghost:#f1ece0;
    --band:linear-gradient(180deg,#e9d6a2 0%,#c9a45a 45%,#a77c33 100%);
  }
  *{box-sizing:border-box;margin:0;padding:0}
  html,body{width:1200px;height:961px;overflow:hidden;background:var(--backdrop)}
  .stage{position:relative;width:1200px;height:961px;background:var(--backdrop)}
  .sheet{position:absolute;background:var(--paper);box-shadow:2px 3px 8px rgba(0,0,0,.35);overflow:hidden}
  .brand{display:flex;align-items:flex-start;gap:10px;font-family:"Cormorant Garamond",serif;font-weight:500;color:var(--gold-dark)}
  .brand-square{width:36px;height:36px;background:var(--gold);flex:none;margin-top:4px}
  .brand-name{line-height:1}
  .brand-name .pre{font-size:16px;letter-spacing:.5px}
  .brand-name .main{font-size:25px;letter-spacing:.3px;display:block;margin-top:2px;white-space:nowrap}
  .tagline{font-family:"Lato",sans-serif;font-size:10.5px;color:var(--ink);margin-top:5px;letter-spacing:.3px}
  .practice{font-family:"Cormorant Garamond",serif;font-weight:500;color:var(--gold-dark);letter-spacing:1.5px;text-transform:uppercase;white-space:nowrap}
  .ghost-pattern{position:absolute;background:linear-gradient(135deg,var(--ghost),#faf7f0)}
  .gold-band{position:absolute;left:0;right:0;bottom:0;background:var(--band);font-family:"Lato",sans-serif;color:#fff;white-space:nowrap}

  /* letterhead */
  .letterhead{left:21px;top:117px;width:576px;height:779px}
  .letterhead .brand{position:absolute;left:110px;top:28px}
  .letterhead .ghost-pattern{left:0;top:590px;width:230px;height:200px}
  .letterhead .practice{position:absolute;left:110px;top:670px;font-size:14px}
  .letterhead .gold-band{height:90px;padding:16px 0 0 110px;font-size:10px;line-height:16px;border-top:2px solid var(--gold-light)}

  /* envelope */
  .envelope{left:532px;top:221px;width:647px;height:356px;z-index:2}
  .envelope .brand{position:absolute;left:24px;top:22px}
  .envelope .practice{position:absolute;left:70px;top:104px;font-size:12px}
  .envelope .ghost-pattern{left:0;top:130px;width:150px;height:164px}
  .envelope .gold-band{height:62px;text-align:right;padding:22px 24px 0 0;font-size:11px;border-top:2px solid var(--gold-light)}

  /* business card */
  .card{left:688px;top:714px;width:286px;height:156px;background:var(--band);z-index:3;font-family:"Lato",sans-serif;color:#fff;font-size:7.5px;line-height:11px}
  .card .left{position:absolute;left:16px;top:16px}
  .card .right{position:absolute;right:16px;top:16px;text-align:right}
  .card .nm{font-family:"Cormorant Garamond",serif;font-size:13px;font-weight:500;margin-bottom:4px;line-height:1.1}
  .card .practice{color:#fff;font-size:8px;position:absolute;left:16px;bottom:14px}
</style>
</head>
<body>
<div class="stage">

  <section class="sheet letterhead">
    <div class="brand">
      <div class="brand-square"></div>
      <div>
        <div class="brand-name"><span class="pre">LAW OFFICE OF</span><span class="main">DOROTHY B HALLBROOK</span></div>
        <div class="tagline">Clarity · Diligence · Resolve</div>
      </div>
    </div>
    <div class="ghost-pattern" role="img" aria-label="Faint decorative key pattern watermark"></div>
    <div class="practice">Appeals – Commercial Litigation</div>
    <div class="gold-band">
      1420 W. Cedar Ridge Road • Mesa, Arizona 85201 • Phone: 480-555-0142 • Fax: 480-555-0143<br>
      E-mail: dot.hallbrook@example.net • www.hallbrooklaw.example
    </div>
  </section>

  <section class="sheet envelope">
    <div class="brand">
      <div class="brand-square"></div>
      <div>
        <div class="brand-name"><span class="pre">LAW OFFICE OF</span><span class="main">DOROTHY B HALLBROOK</span></div>
        <div class="tagline">Clarity · Diligence · Resolve</div>
      </div>
    </div>
    <div class="practice">Appeals – Commercial Litigation</div>
    <div class="ghost-pattern" role="img" aria-label="Faint decorative key pattern watermark"></div>
    <div class="gold-band">1420 W. Cedar Ridge Road • Mesa, Arizona 85201</div>
  </section>

  <section class="sheet card">
    <div class="left">
      <div class="nm">Dorothy B Hallbrook</div>
      Attorney at Law<br>
      1420 W. Cedar Ridge Road<br>
      Mesa, Arizona 85201
    </div>
    <div class="right">
      Phone 480-555-0142<br>
      Fax 480-555-0143<br>
      Cell 480-555-0198<br>
      dot.hallbrook@example.net
    </div>
    <div class="practice">Appeals – Commercial Litigation</div>
  </section>

</div>
</body>
</html>
```